KTR Football Academy Flyer

Flyer for a full page of a yearbook ( dimensions below ) along with all the contents/photos for the flyer.
Width - 210 mm
Height - 297 mm
Please also see attached the previous flyer which we feel is in need of an upgrade !
Flyer will also be used on social media pages.
Creating next level athletes !
Providing a platform and the correct environment for young football players to develop and fulfil their potential.
Why choose KTR Football Academy
- Multiple programs for everyone
- WAPL qualified & experienced coaches
- Safe and fun environment
- All coaches police checked
- Coaches Emergency First Aid Qualified
- Coaches Safeguarding Children Qualified
- Develop new skills
- Make new friends
- Improve your fitness
REGISTER NOW!
www.brightfieldathletix.example
+968 912 40637
Instagram/Facebook - ktrfootballacademy

```html
<!DOCTYPE html>
<html lang="en">
<head>
<meta charset="utf-8">
<title>KTR Football Academy Flyer</title>
<link href="https://fonts.googleapis.com/css2?family=Anton&family=Poppins:wght@400;500;600;700&family=Roboto+Condensed:wght@700&display=swap" rel="stylesheet">
<style>
  :root{
    --stage:#dcdde3;
    --green:#6cbf46;
    --green-deep:#3f9a3a;
    --slate:#5e6062;
    --slate-dark:#48494b;
    --body:#3c3d3f;
    --white:#ffffff;
  }
  *{margin:0;padding:0;box-sizing:border-box}
  html,body{width:1200px;height:856px;overflow:hidden;background:var(--stage)}
  .stage{position:relative;width:1200px;height:856px}
  .flyer{position:absolute;left:317px;top:28px;width:566px;height:800px;background:var(--white);overflow:hidden;box-shadow:0 6px 18px rgba(0,0,0,.18)}
  .flyer-shapes{position:absolute;inset:0;width:566px;height:800px}

  .headline{position:absolute;left:0;top:0;width:566px;height:220px;font-family:"Anton",Impact,sans-serif;font-weight:400}
  .headline span{position:absolute;left:26px;line-height:1;white-space:nowrap;transform-origin:left top}
  .headline-creating{top:21px;font-size:68px;color:transparent;-webkit-text-stroke:1.5px var(--white);transform:scaleX(1.25)}
  .headline-next{top:86px;font-size:98px;color:var(--green);transform:scaleX(1.34)}
  .headline-level{top:171px;font-size:40px;color:var(--white);transform:scaleX(1.18)}

  .mission{position:absolute;left:247px;top:458px;font-family:"Poppins",sans-serif;font-size:15.4px;line-height:22px;color:var(--white);font-weight:500;white-space:nowrap}
  .mission em{font-style:normal;color:var(--green);font-weight:600;font-size:18px}

  .why{position:absolute;left:251px;top:567px;font-family:"Poppins",sans-serif}
  .why-title{font-size:14px;line-height:18px;font-weight:700;color:var(--green);margin-bottom:2px}
  .why-list{list-style:none}
  .why-list li{position:relative;padding-left:19px;font-size:9.4px;line-height:17.4px;color:var(--body);font-weight:500;letter-spacing:.2px}
  .why-list li::before{content:"";position:absolute;left:0;top:4px;width:10px;height:10px;border-radius:2px;background:var(--slate)}

  .register{position:absolute;left:18px;top:755px;font-family:"Anton",Impact,sans-serif;font-size:16px;line-height:18px;color:var(--green);letter-spacing:.3px}
  .web{position:absolute;left:96px;top:765px;display:flex;align-items:center;gap:5px;font-family:"Roboto Condensed",sans-serif;font-weight:700;font-size:15px;line-height:18px;color:var(--white)}
  .phone{position:absolute;left:336px;top:765px;display:flex;align-items:center;gap:5px;font-family:"Roboto Condensed",sans-serif;font-weight:700;font-size:14px;line-height:18px;color:var(--white)}
  .social{position:absolute;left:470px;top:768px;display:flex;align-items:center;gap:4px;font-family:"Poppins",sans-serif;font-weight:500;font-size:7px;line-height:12px;color:var(--white);white-space:nowrap}
  .social-dot{width:12px;height:12px;border-radius:50%;background:var(--green);flex:none}
</style>
</head>
<body>
<div class="stage">
  <main class="flyer">
    <svg class="flyer-shapes" viewBox="0 0 566 800">
      <defs>
        <linearGradient id="pitchGrad" x1="0" y1="0" x2="0" y2="1">
          <stop offset="0" stop-color="#141a14"/>
          <stop offset=".5" stop-color="#2b3a27"/>
          <stop offset="1" stop-color="#5a8a3f"/>
        </linearGradient>
        <linearGradient id="kitGrad" x1="0" y1="0" x2="0" y2="1">
          <stop offset="0" stop-color="#c9a98e"/>
          <stop offset=".25" stop-color="#2f8a3e"/>
          <stop offset=".7" stop-color="#277a35"/>
          <stop offset="1" stop-color="#e6e6e6"/>
        </linearGradient>
        <linearGradient id="teamGrad" x1="0" y1="0" x2="1" y2="0">
          <stop offset="0" stop-color="#2f8a3e"/>
          <stop offset=".5" stop-color="#3d9a48"/>
          <stop offset="1" stop-color="#2b7f38"/>
        </linearGradient>
      </defs>

      <rect class="slate-band" x="0" y="0" width="566" height="563" fill="var(--slate)"/>
      <path class="chevron-frame" d="M0,0 H566 V222 L286,452 Q150,360 52,300 Q18,275 0,270 Z" fill="var(--white)"/>
      <path class="hero-photo" role="img" aria-label="Photo: two young players in green and lilac kits contest the ball on a floodlit pitch"
            d="M0,0 H566 V198 L284,432 Q150,330 60,268 Q22,240 0,222 Z" fill="url(#pitchGrad)"/>

      <rect class="kids-photo" role="img" aria-label="Photo: two young academy players in green kit standing with a foot on a football"
            x="34" y="372" width="196" height="212" rx="30" fill="url(#kitGrad)"/>

      <g class="team-photo" transform="rotate(-9 125 650)">
        <rect x="28" y="598" width="198" height="112" fill="#8a8b8d"/>
        <rect role="img" aria-label="Photo: academy squad in green kit celebrating with medals and a trophy"
              x="24" y="594" width="198" height="112" fill="url(#teamGrad)"/>
      </g>

      <rect class="footer-base" x="0" y="749" width="566" height="51" fill="var(--white)"/>
      <polygon class="footer-band" points="108,749 566,749 566,800 80,800" fill="var(--slate-dark)"/>
      <line x1="0" y1="747" x2="108" y2="747" stroke="var(--slate)" stroke-width="1.5"/>
      <polygon class="phone-band" points="330,757 462,757 456,789 322,789" fill="var(--green-deep)"/>
      <polygon class="social-band" points="464,749 566,749 566,800 456,800" fill="#3f4042"/>
    </svg>

    <h1 class="headline">
      <span class="headline-creating">Creating</span>
      <span class="headline-next">NEXT</span>
      <span class="headline-level">level athletes</span>
    </h1>

    <p class="mission">Providing a <em>Platform</em> and the<br>correct <em>Environment</em> for young<br>football <em>Players</em> to develop and<br>fulfil their <em>Potential</em>.</p>

    <section class="why">
      <h2 class="why-title">Why choose KTR Football Academy</h2>
      <ul class="why-list">
        <li>Multiple programs for everyone</li>
        <li>WAPL qualified &amp; experienced coaches</li>
        <li>Safe and fun environment</li>
        <li>All coaches police checked</li>
        <li>Coaches Emergency First Aid Qualified</li>
        <li>Coaches Safeguarding Children Qualified</li>
        <li>Develop new skills</li>
        <li>Make new friends</li>
        <li>Improve your fitness</li>
      </ul>
    </section>

    <div class="register">REGISTER<br>NOW!</div>

    <div class="web">
      <svg width="12" height="12" viewBox="0 0 12 12" aria-hidden="true"><g fill="none" stroke="#fff" stroke-width="1"><circle cx="6" cy="6" r="5.2"/><ellipse cx="6" cy="6" rx="2.3" ry="5.2"/><line x1="0.8" y1="6" x2="11.2" y2="6"/></g></svg>
      <span>brightfieldathletix.example</span>
    </div>

    <div class="phone">
      <svg width="12" height="12" viewBox="0 0 12 12" aria-hidden="true"><path d="M2.5 1 L4.5 1 L5.3 3.6 L4 4.6 Q5 7 7.4 8 L8.4 6.7 L11 7.5 L11 9.5 Q10.5 11 9 11 Q1 10 1 3 Q1 1.5 2.5 1 Z" fill="none" stroke="#fff" stroke-width="1"/></svg>
      <span>+968 912 40637</span>
    </div>

    <div class="social">
      <span class="social-dot"></span>
      <span>ktrfootballacademy</span>
    </div>
  </main>
</div>
</body>
</html>
```